" Auxilia estrangeiros e brasileiros em mudança ao Rio de Janeiro para encontrar imóvel para alugar, mobiliar, contratar serviços de luz, telefone, TV e internet e manutenção. Também fornecemos treinamentos interculturais para adaptação. "

```html
<!DOCTYPE html>
<html lang="pt-BR">
<head>
<meta charset="utf-8">
<title>Assinatura de e-mail — Lumacasa</title>
<link rel="stylesheet" href="https://fonts.googleapis.com/css2?family=Cormorant+Garamond:wght@500&family=Open+Sans:wght@400;600;700&display=swap">
<style>
  :root {
    --page-bg: #eef1f5;
    --blue-deep: #1c4a86;
    --blue-mid: #2a64ad;
    --blue-light: #4f86c6;
    --ink: #1d1d1f;
    --ink-soft: #4a5568;
    --divider: #c9d3df;
    --haze: #e6ebf1;
  }
  * { margin: 0; padding: 0; box-sizing: border-box; }
  html, body {
    width: 1200px;
    height: 1200px;
    overflow: hidden;
    background: var(--page-bg);
  }
  .signature {
    position: absolute;
    left: 0;
    top: 470px;
    width: 1200px;
    height: 260px;
  }
  .signature-shape {
    position: absolute;
    inset: 0;
  }
  .brand-name {
    position: absolute;
    left: 110px;
    top: 102px;
    font-family: "Open Sans", sans-serif;
    font-weight: 600;
    font-size: 60px;
    letter-spacing: -1px;
    color: #ffffff;
    line-height: 1;
  }
  .person {
    position: absolute;
    left: 552px;
    top: 104px;
    width: 260px;
  }
  .person-name {
    font-family: "Cormorant Garamond", serif;
    font-weight: 500;
    font-size: 29px;
    letter-spacing: 0.5px;
    color: var(--ink);
    line-height: 1;
    white-space: nowrap;
  }
  .person-role {
    margin-top: 4px;
    font-family: "Open Sans", sans-serif;
    font-weight: 700;
    font-size: 19px;
    color: var(--ink);
    line-height: 1.2;
  }
  .contacts {
    position: absolute;
    left: 868px;
    top: 46px;
    list-style: none;
    font-family: "Open Sans", sans-serif;
    font-size: 18px;
    color: var(--ink-soft);
    line-height: 1.25;
  }
  .contact-item {
    display: flex;
    align-items: center;
    gap: 14px;
    margin-bottom: 12px;
  }
  .contact-icon {
    flex: 0 0 38px;
    width: 38px;
    height: 38px;
  }
</style>
</head>
<body>
  <section class="signature" aria-label="Assinatura de e-mail">
    <svg class="signature-shape" width="1200" height="260" viewBox="0 0 1200 260">
      <defs>
        <linearGradient id="panelBlue" x1="0" y1="0" x2="1" y2="1">
          <stop offset="0" stop-color="#1c4a86"/>
          <stop offset="0.6" stop-color="#2a64ad"/>
          <stop offset="1" stop-color="#4f86c6"/>
        </linearGradient>
        <linearGradient id="cardHaze" x1="0" y1="0" x2="0" y2="1">
          <stop offset="0" stop-color="#ffffff"/>
          <stop offset="1" stop-color="#e6ebf1"/>
        </linearGradient>
      </defs>
      <path d="M40 20 H1120 Q1180 20 1180 80 V240 H40 Q20 240 20 220 V40 Q20 20 40 20 Z"
            fill="url(#cardHaze)" role="img" aria-label="Silhueta suave de prédios da cidade ao fundo"/>
      <path d="M60 20 H440 Q500 20 520 80 L540 200 Q548 240 500 240 H60 Q20 240 20 200 V60 Q20 20 60 20 Z"
            fill="url(#panelBlue)" role="img" aria-label="Silhueta de prédios da cidade em tons de azul"/>
      <line x1="836" y1="50" x2="836" y2="210" stroke="#c9d3df" stroke-width="2"/>
    </svg>

    <div class="brand-name">Lumacasa</div>

    <div class="person">
      <p class="person-name">NOME COMPLETO</p>
      <p class="person-role">Cargo</p>
    </div>

    <ul class="contacts">
      <li class="contact-item">
        <svg class="contact-icon" viewBox="0 0 38 38" aria-hidden="true">
          <circle cx="19" cy="19" r="17" fill="none" stroke="var(--blue-mid)" stroke-width="2"/>
          <path d="M13 11 l4 0 l1.5 4 l-2.5 1.5 q1.5 3.5 5 5 l1.5 -2.5 l4 1.5 l0 4 q-10 1 -13.5 -13.5 z" fill="var(--blue-mid)"/>
        </svg>
        <span>(xx) xxxx-xxxx</span>
      </li>
      <li class="contact-item">
        <svg class="contact-icon" viewBox="0 0 38 38" aria-hidden="true">
          <circle cx="19" cy="19" r="17" fill="none" stroke="var(--blue-mid)" stroke-width="2"/>
          <path d="M19 9 a6.5 6.5 0 0 1 6.5 6.5 c0 5 -6.5 12.5 -6.5 12.5 s-6.5 -7.5 -6.5 -12.5 A6.5 6.5 0 0 1 19 9 z" fill="var(--blue-mid)"/>
          <circle cx="19" cy="15.5" r="2.5" fill="#ffffff"/>
        </svg>
        <span>Seu endereço - Bairro<br>Cidade - Estado<br>CEP 000-0000</span>
      </li>
      <li class="contact-item">
        <svg class="contact-icon" viewBox="0 0 38 38" aria-hidden="true">
          <circle cx="19" cy="19" r="17" fill="none" stroke="var(--blue-mid)" stroke-width="2"/>
          <rect x="10" y="13" width="18" height="12" rx="1.5" fill="var(--blue-mid)"/>
          <path d="M10.5 13.5 L19 20 L27.5 13.5" fill="none" stroke="#ffffff" stroke-width="1.6"/>
        </svg>
        <span>seuemail@exemplo.com</span>
      </li>
    </ul>
  </section>
</body>
</html>
```